Homepage für Unternehmensberatung
Zielgruppe
Wir sind eine Unternehmensberatung mit einem klaren Branchenfokus auf Banken / Finanzdienstleister.
Unsere Dienstleistungsprodukte lassen sich grob in folgende Themencluster unterteilen:
1)Strategieentwicklung
o IT-Strategie, IT-Architektur, IT-Bebauungsplan
2) Projektmanagement
o Projektportfoliomgmt., Programmmgmt., Projektmanagement, Projektcontrolling
3) Fachberatung
o Bankfachliche IT- Beratung mit Schwerpunkten Kredit, Wertpapiergeschäft,
Bankenaufsichtsrecht, Liquiditätsmanagement
o Anforderungsmanagement inkl. Aufbau von Bewertungs- und Priorisierungsmethoden
4) Prozessberatung/-optimierung
o Prozessanalyse, Prozessdesign, Prozessdokumentation
o Prozessoptimierung auf Basis etablierter Messmethoden
Unser Firmenname Lindenhofer hat für uns eine Doppelbedeutung:
1. Im Außenverhältnis: Wir verstehen uns als Lindenhofer unserer Kunden
2. Im Innenverhältnis: Wir pflegen einen partnerschaftlichen Umgang mit unseren
Mitarbeitern (Teamarbeit)
Aktuell sind wir ein kleines aber feines Team von erfahrenen und hochmotivierten Kollegen. Unsere Mitarbeiter sind ehemalige Führungskräfte sowie erfahrenen Unternehmensberater.
Aufgabenstellung
Entwurf / Design von 2 Seiten:
1. Seite / Startseite:
Simple und elegante Darstellung der oben genannten 4 Themencluster (z.B. Bild/Piktogramm, Textkasten) sowie einer Navigationsmöglichkeit zu folgenden Detailsichten:
• Unternehmen
• Beratungsangebot (siehe Themencluster)
• Partnerunternehmen
• Kontakt
2. Seite / 2. Ebene:
Entwurf einer Möglichkeit zur Erläuterung/Darstellung von Inhalten der Startseite.
Die Themencluster sollten auf jeder Ebene immer „anklickbar“/ zu sehen sein.
Logo
Das angehängte Logo ist in die Website einzubinden. Stil und Farben sollen übernommen werden bzw. sind Basis für das Design.
Lizenzen
Lizenz für eingesetzte Fotos und Illustrationen soll enthalten / Open-Source sein. Wenn nicht dann bitte zusätzliche Kosten angeben.

```html
<!DOCTYPE html>
<html lang="en">
<head>
<meta charset="utf-8">
<title>Lindenhofer – Management Consulting</title>
<link href="https://fonts.googleapis.com/css2?family=Ubuntu:wght@300;400;500&display=swap" rel="stylesheet">
<style>
:root{
  --blue:#1d74b2;
  --band:#4b9ccb;
  --band-btn:#3d8cbd;
  --ink:#2b3846;
  --text:#3a3a3a;
  --rule:#cfd3d6;
  --soft:#f8f7f7;
  --footer:#5e686f;
  --footer-dark:#4e585f;
  --footer-text:#e4e8eb;
  --nav-active:#5f6a71;
  --date:#8d9399;
}
*{margin:0;padding:0;box-sizing:border-box}
html,body{width:798px;height:1200px;overflow:hidden}
body{font-family:"Ubuntu",sans-serif;color:var(--text);background:#fff;position:relative}
.abs{position:absolute}

/* header */
.header{left:0;top:0;width:798px;height:54px;background:#fff;border-bottom:1px solid #e3e3e3}
.brand{left:78px;top:7px;display:flex;align-items:center;gap:8px}
.brand-dot{width:41px;height:41px;border-radius:50%;background:var(--blue)}
.brand-name{font-size:17px;font-weight:400;color:var(--blue);letter-spacing:.3px}
.nav a{position:absolute;top:16px;font-size:7.8px;color:#222;text-decoration:none;line-height:19px;white-space:nowrap}
.nav a.active{background:var(--nav-active);color:#fff;padding:0 4px;border-radius:2px}

/* hero */
.hero{left:0;top:54px;width:798px;height:347px;background:linear-gradient(100deg,#2a211d 0%,#4d3b30 30%,#6b5242 55%,#3a2a22 80%,#241a16 100%)}
.band{left:0;top:401px;width:798px;height:41px;background:var(--band);color:#fff}
.band h2{position:absolute;left:78px;top:9px;font-size:10.2px;font-weight:300;letter-spacing:.2px}
.band p{position:absolute;left:78px;top:24px;font-size:6.8px;font-weight:300}
.hire{position:absolute;left:628px;top:9px;width:76px;height:23px;background:var(--band-btn);border:1px solid #a9d0e8;font-size:10.5px;text-align:center;line-height:21px;font-weight:400}

/* why */
.why{left:0;top:442px;width:798px;height:188px;background:var(--soft)}
.why h2{position:absolute;left:79px;top:19px;font-size:13.4px;font-weight:500;color:var(--ink)}
.why .copy{position:absolute;left:78px;top:43px;width:368px;font-size:7.7px;line-height:13.45px;color:#333}
.why .lead{position:absolute;left:78px;top:131px;font-size:8.2px;font-weight:500;color:#222}
.btn{position:absolute;left:78px;top:152px;width:59px;height:21px;background:var(--blue);color:#fff;font-size:8px;line-height:21px;text-align:center;border-radius:2px}
.logo-box{position:absolute;left:454px;top:37px;width:251px;height:108px;background:#fff;border:1px solid #e2e2e2;box-shadow:0 1px 2px rgba(0,0,0,.06);display:flex;align-items:center;justify-content:center;gap:10px}
.logo-box .brand-dot{width:48px;height:48px}
.logo-box .brand-name{font-size:21px}

/* offer */
.section-title{font-size:13.4px;font-weight:500;color:var(--ink)}
.offer-title{left:79px;top:653px}
.rule{height:1px;background:var(--rule)}
.card{position:absolute;top:685px;width:146px}
.card .pic{width:146px;height:80px;border:2px solid #fff;outline:1px solid #ddd}
.card h3{margin-top:10px;font-size:7.4px;font-weight:400;color:var(--blue);white-space:nowrap}
.card p{margin-top:3px;font-size:6.1px;line-height:8.2px;color:#333}
.card p span{color:var(--blue)}

/* help */
.help-pic{left:78px;top:883px;width:144px;height:80px;border:2px solid #fff;outline:1px solid #ddd;background:linear-gradient(120deg,#6f7f8c,#9aa6ae 45%,#2b3a5a 75%,#1d2a44)}
.help-sub{left:229px;top:882px;font-size:7.4px;color:var(--blue)}
.help-text{left:229px;top:894px;width:143px;font-size:6.1px;line-height:8.1px;color:#333;text-align:justify}
.help-text p+p{margin-top:6px}
.bullets{left:78px;top:972px;list-style:none;font-size:6.2px;color:#333}
.bullets li{height:13.45px;padding-left:9px;position:relative}
.bullets li::before{content:"›";position:absolute;left:0;top:-2px;font-size:9px;color:var(--blue)}
.divider{left:389px;top:843px;width:1px;height:197px;background:var(--rule)}

/* news */
.news{position:absolute;left:409px;width:295px}
.date{position:absolute;left:0;top:0;width:38px;height:34px;background:var(--date);border:2px solid #e5e7e9;outline:1px solid #cfd3d6;color:#fff;text-align:center}
.date b{display:block;font-size:10px;font-weight:500;margin-top:3px;line-height:11px}
.date small{display:block;font-size:7px;font-weight:500}
.news h4{position:absolute;left:45px;top:-4px;font-size:7.4px;font-weight:400;color:var(--blue);white-space:nowrap}
.news p{position:absolute;left:45px;top:6px;width:248px;font-size:6.1px;line-height:8.2px;color:#333;text-align:justify}

/* footer */
.footer{left:0;top:1084px;width:798px;height:91px;background:var(--footer);color:var(--footer-text)}
.footer .brand{left:78px;top:14px}
.footer .brand-dot{background:#fff;width:43px;height:43px}
.footer .brand-name{color:#fff;font-size:17px}
.f-col{position:absolute;font-size:7.4px;line-height:10.3px;font-weight:300}
.f-col .cap{font-weight:400;text-transform:uppercase}
.f-links a{position:absolute;font-size:7.6px;color:var(--footer-text);text-decoration:none;font-weight:300;white-space:nowrap}
.base{left:0;top:1175px;width:798px;height:25px;background:var(--footer-dark);color:var(--footer-text);font-size:7.6px;font-weight:300}
.base span{position:absolute;top:6px}
</style>
</head>
<body>

<header class="header abs">
  <div class="brand abs"><div class="brand-dot"></div><div class="brand-name">Lindenhofer</div></div>
  <nav class="nav">
    <a class="active" style="left:379px">COMPANY</a>
    <a style="left:452px">CONSULTING SERVICE</a>
    <a style="left:562px">PARTNER COMPANIES</a>
    <a style="left:668px">CONTACT</a>
  </nav>
</header>

<div class="hero abs" role="img" aria-label="Photo: smiling consultant in a dark suit gesturing toward colleagues meeting at a table in an office"></div>

<section class="band abs">
  <h2>PROGRESSIVE BUSINESS THINKING</h2>
  <p>Lorem ipsum dolor sit amet, consectetur adipiscing elit, sed do eiusmod tempor incididunt ut labore et dolore magna aliqua Ut eation ullamco laboris nisi.</p>
  <div class="hire">HIRE US !</div>
</section>

<section class="why abs">
  <h2>WHY CHOOSE LINDENHOFER GMBH</h2>
  <p class="copy">Sed ut perspiciatis unde omnis iste natus error sit voluptatem accusantium doloremque laudantium, tam rem aperiam, eaque ipsa quae ab illo inventore veritatis et quasi architecto beatae vitae dicta sunt licabo. Nemo enim ipsam voluptatem quia voluptas sit aspernatur aut odit aut fugit, sed quia onsequuntmagni dolores eos qui ratione voluptatem sequi nesciunt. Neque porro quisquam est, qui dolorem ipsum quia dolor sit amet, consectetur, adipisci velit, sed quia non numquam eius modi tempora incidunt ut labore et dolore magnam aliquam quaerat voluptatem.</p>
  <p class="lead">Find out how your business can grow with Lindenhofer.</p>
  <div class="btn">Learn More</div>
  <div class="logo-box"><div class="brand-dot"></div><div class="brand-name">Lindenhofer</div></div>
</section>

<h2 class="section-title abs offer-title">WHAT WE OFFER</h2>
<div class="rule abs" style="left:78px;top:671px;width:627px"></div>

<article class="card" style="left:78px">
  <div class="pic" role="img" aria-label="Photo: businessman drawing rising arrows" style="background:linear-gradient(120deg,#6f7f8c,#9aa6ae 45%,#2b3a5a 75%,#1d2a44)"></div>
  <h3>STRATEGY DEVELOPMENT</h3>
  <p>Integer fermentum odio sed vestibulum viverra. Integer id lectus non ligula fermentum ultricies ut rutrum mauris. Ut mauris urna, dictum ultrices tellus ut <span>Read More...</span></p>
</article>
<article class="card" style="left:238px">
  <div class="pic" role="img" aria-label="Photo: businessman beside a growth chart" style="background:linear-gradient(110deg,#c9d4dc,#e9ecee 45%,#b0bcc6 70%,#8997a3)"></div>
  <h3>PROJECT MANAGEMENT</h3>
  <p>Integer fermentum odio sed vestibulum viverra. Integer id lectus non ligula fermentum ultricies ut rutrum mauris. Ut mauris urna, dictum ultrices tellus ut <span>Read More...</span></p>
</article>
<article class="card" style="left:398px">
  <div class="pic" role="img" aria-label="Photo: open hands of a businessman presenting" style="background:linear-gradient(110deg,#2d4f8a,#8ea6c6 35%,#e3e7ea 65%,#f1f2f3)"></div>
  <h3>PROFESSIONAL CONSULTING SERVICE</h3>
  <p>Integer fermentum odio sed vestibulum viverra. Integer id lectus non ligula fermentum ultricies ut rutrum mauris. Ut mauris urna, dictum ultrices tellus ut <span>Read More...</span></p>
</article>
<article class="card" style="left:560px">
  <div class="pic" role="img" aria-label="Photo: hand touching a glowing question mark surrounded by how, what, when, where, who" style="background:radial-gradient(circle at 50% 45%,#4aa7d2,#1c4e72 55%,#0c1f33)"></div>
  <h3>PROCESS CONSULTING &amp; OPTIMIZATION</h3>
  <p>Integer fermentum odio sed vestibulum viverra. Integer id lectus non ligula fermentum ultricies ut rutrum mauris. Ut mauris urna, dictum ultrices tellus ut <span>Read More...</span></p>
</article>

<h2 class="section-title abs" style="left:79px;top:851px">HOW CAN SAFETY CONSULTANTS HELP YOU?</h2>
<div class="rule abs" style="left:78px;top:869px;width:296px"></div>
<div class="help-pic abs" role="img" aria-label="Photo: businessman drawing rising arrows"></div>
<h3 class="help-sub abs" style="font-weight:400">SUB HEADING FOR THIS SECTION</h3>
<div class="help-text abs">
  <p>At vero eos et accusamus et iusto odio dignissimos ducimus qui blanditiis praesentium voluptatum deleniti atque.</p>
  <p>Corrupti quos dolores et quas molestias excepturi sint occaecati cupiditate non provident, similique sunt in culpa qui officia deserunt mollitia animi, id est laborum.</p>
</div>
<ul class="bullets abs">
  <li>Aenean ornare justo et erat lobortis posuere.</li>
  <li>Aliquam sed sapien id risus mollis mattis at non magna.</li>
  <li>Ut non lacus non sapien egestas sollicitudin a vitae quam.</li>
  <li>Proin porttitor nisi non eros eleifend, ac ullamcorper quam tempus.</li>
  <li>Praesent scelerisque ex eu dolor gravida fermentum.</li>
</ul>
<div class="divider abs"></div>

<h2 class="section-title abs" style="left:410px;top:851px">LATEST NEWS</h2>
<div class="rule abs" style="left:409px;top:869px;width:296px"></div>

<div class="news" style="top:879px">
  <div class="date"><b>27</b><small>APR</small></div>
  <h4>Duis posuere consectetur pellentesqe</h4>
  <p>Sed nisi turpis pellentesque at ultrices in dapibus in magnatr. Nunc easi diam risus placerat ut scelerisque et suscipit euter ante. Nullam vitae dolor ullcper felises cursus gravida.</p>
</div>
<div class="news" style="top:934px">
  <div class="date"><b>27</b><small>APR</small></div>
  <h4>Duis posuere consectetur pellentesqe</h4>
  <p>Sed nisi turpis pellentesque at ultrices in dapibus in magnatr. Nunc easi diam risus placerat ut scelerisque et suscipit euter ante. Nullam vitae dolor ullcper felises cursus gravida.</p>
</div>
<div class="news" style="top:984px">
  <div class="date"><b>27</b><small>APR</small></div>
  <h4>Duis posuere consectetur pellentesqe</h4>
  <p>Sed nisi turpis pellentesque at ultrices in dapibus in magnatr. Nunc easi diam risus placerat ut scelerisque et suscipit euter ante. Nullam vitae dolor ullcper felises cursus gravida.</p>
</div>

<footer class="footer abs">
  <div class="brand abs"><div class="brand-dot"></div><div class="brand-name">Lindenhofer</div></div>
  <div class="f-col" style="left:126px;top:52px">
    <div class="cap">Lindenhofer Consulting GmbH</div>
    <div>Birkenstieg 42</div>
    <div>31547 Haldenau</div>
  </div>
  <div class="f-col" style="left:351px;top:22px">
    <div class="cap">Managing Directors:</div>
    <div>Malte Ostrander, Fenja Kuhrig</div>
    <div style="margin-top:10px" class="cap">Amtsgericht Haldenau - HRB 481207</div>
    <div>Tax Office Haldenau - 23/418/50612</div>
  </div>
  <div class="f-links">
    <a style="left:536px;top:22px">USEFUL LINKS:</a>
    <a style="left:536px;top:38px">» Home</a>
    <a style="left:536px;top:54px">» Company</a>
    <a style="left:628px;top:22px">» Consulting Service</a>
    <a style="left:628px;top:38px">» Partners Companies</a>
    <a style="left:628px;top:54px">» Contact Us</a>
  </div>
</footer>
<div class="base abs">
  <span style="left:79px">Copyrights 2014,&nbsp; Lindenhofer gmbh. All rights reserved.</span>
  <span style="left:619px">Imprint&nbsp; //&nbsp; Privacy Policy</span>
</div>

</body>
</html>
```